Business Card Design Project

for a second hand vintage clothing store. shop name is The Velvet Cupboard

Cards to be double sided

The name on the card is Joanna Whitfield

Information to put on card:

The Velvet Cupboard
Joanna Whitfield (no job title)
42/871 Dunmore St, Glenwick, Sydney, NSW, 2009.
Mobile: 0412 905 261
Email: thevelvetcupboard@mailbox.com.au
Web: www.thevelvetcupboard.com.au

Target Market(s)

Women looking at vintage clothing

Industry/Entity Type

Clothing

```html
<!DOCTYPE html>
<html lang="en">
<head>
<meta charset="utf-8">
<title>The Velvet Cupboard — Business Card</title>
<link rel="stylesheet" href="https://fonts.googleapis.com/css2?family=Libre+Baskerville:ital,wght@0,400;1,400;1,700&family=Jost:wght@400&display=swap">
<style>
  :root {
    --backdrop: #95a0a6;
    --plum: #451134;
    --plum-ink: #4a1238;
    --gold: #ece493;
    --paper: #ffffff;
    --shadow: rgba(0, 0, 0, 0.75);
  }
  * { margin: 0; padding: 0; box-sizing: border-box; }
  html, body {
    width: 1200px;
    height: 900px;
    overflow: hidden;
  }
  body {
    position: relative;
    background: var(--backdrop);
  }
  .card {
    position: absolute;
    left: 70px;
    width: 1063px;
    height: 281px;
    box-shadow: 6px 7px 4px var(--shadow);
  }
  .card-front {
    top: 144px;
    background: var(--plum);
  }
  .card-back {
    top: 479px;
    background: var(--paper);
  }
  .brand-name {
    position: absolute;
    left: 50px;
    top: 104px;
    font-family: "Libre Baskerville", Georgia, serif;
    font-weight: 400;
    font-size: 40px;
    color: var(--gold);
    white-space: nowrap;
  }
  .tagline {
    position: absolute;
    left: 1000px;
    top: 34px;
    writing-mode: vertical-rl;
    font-family: "Libre Baskerville", Georgia, serif;
    font-style: italic;
    font-size: 19px;
    letter-spacing: 2.5px;
    color: var(--gold);
    white-space: nowrap;
  }
  .back-title {
    position: absolute;
    left: 76px;
    top: 62px;
    font-family: "Libre Baskerville", Georgia, serif;
    font-style: italic;
    font-weight: 700;
    font-size: 23px;
    letter-spacing: 1.5px;
    color: var(--plum-ink);
    white-space: nowrap;
  }
  .contact {
    position: absolute;
    right: 49px;
    top: 135px;
    list-style: none;
    text-align: right;
    font-family: "Jost", "Century Gothic", sans-serif;
    font-size: 18.5px;
    line-height: 23.8px;
    text-transform: uppercase;
    color: var(--plum-ink);
    white-space: nowrap;
  }
</style>
</head>
<body>
  <section class="card card-front" aria-label="Card front">
    <h1 class="brand-name">The Velvet Cupboard</h1>
    <p class="tagline">vintage clothing</p>
  </section>

  <section class="card card-back" aria-label="Card back">
    <h2 class="back-title">The Velvet Cupboard</h2>
    <ul class="contact">
      <li>Joanna Whitfield</li>
      <li>42/871 Dunmore St, Glenwick, Sydney, NSW, 2009</li>
      <li>Mob: 0412 905 261</li>
      <li>E: thevelvetcupboard@mailbox.com.au</li>
      <li>www.thevelvetcupboard.com.au</li>
    </ul>
  </section>
</body>
</html>
```